Young, dynamic furniture company needs a new business card design

We require a new business card design for our modern furniture company which supplies furniture and appliances to the property and development market.
Birchlane Furnishing has become one of the leading furniture & appliance suppliers to the property market withing London. With over 10 years experience, we have increased our business to supply not only private landlords and managing agents, but also property developers, housing associations and local councils.
We offer not only a complete range of furniture which includes beds, wardrobes, dining sets and sofas, but also a high quality, full delivery and assembly service to help you with all our furnishing needs.

Target Market(s)

Private landlords, estate agents, letting agents, property management companies

Industry/Entity Type

Business

Contact Information for Business Card

Name,
Title,
Address,
Mobile,
Telephone,
Fax, Website, email address

Font styles to use
Sans Serif

Colors
3176b5
0555a3
85abd2
cfdeed

Requirements
Must have
• All the above information for each of our staff, along with our logo

```html
<!DOCTYPE html>
<html lang="en">
<head>
<meta charset="UTF-8">
<title>Birchlane Furnishing – Business Card</title>
<link rel="stylesheet" href="https://fonts.googleapis.com/css2?family=Poppins:wght@700&family=Roboto:wght@300;400&display=swap">
<style>
  :root {
    --stage: #131a30;
    --navy: #24427a;
    --brand-blue: #3176b5;
    --deep-blue: #0555a3;
    --ink: #1d2233;
    --paper: #ffffff;
    --muted: #cfdeed;
  }
  * { margin: 0; padding: 0; box-sizing: border-box; }
  html, body {
    width: 1200px; height: 900px; overflow: hidden;
    background: var(--stage);
    font-family: "Roboto", Arial, sans-serif;
  }
  .stage { position: relative; width: 1200px; height: 900px; }

  .card {
    position: absolute;
    width: 600px; height: 343px;
    border-radius: 26px;
    box-shadow: 0 18px 40px rgba(0,0,0,.45);
  }
  .card--front { left: 120px; top: 90px; background: var(--navy); color: var(--paper); }
  .card--back  { left: 480px; top: 467px; background: var(--paper); color: var(--ink); }

  /* brand block */
  .brand { display: flex; flex-direction: column; align-items: center; }
  .brand__row { display: flex; align-items: center; gap: 12px; }
  .brand__dot { width: 14px; height: 14px; border-radius: 50%; }
  .brand__name {
    font-weight: 300; text-transform: uppercase; letter-spacing: .5px; line-height: 1;
  }
  .brand__tagline {
    font-weight: 300; text-transform: uppercase; letter-spacing: .4px; margin-top: 5px;
  }

  .card--front .brand { position: absolute; left: 0; right: 0; top: 120px; }
  .card--front .brand__dot { background: var(--paper); }
  .card--front .brand__name { font-size: 30px; }
  .card--front .brand__tagline { font-size: 13px; }
  .card--front .site {
    position: absolute; left: 0; right: 0; top: 228px; text-align: center;
    font-size: 14px; letter-spacing: 2px;
  }

  .card--back .brand { position: absolute; right: 40px; top: 44px; align-items: flex-end; }
  .card--back .brand__dot { background: var(--brand-blue); }
  .card--back .brand__name { font-size: 22px; color: var(--ink); }
  .card--back .brand__tagline { font-size: 10px; color: var(--ink); }

  .contact { position: absolute; left: 44px; bottom: 40px; }
  .contact__name {
    font-family: "Poppins", Arial, sans-serif; font-weight: 700;
    font-size: 30px; color: var(--navy); line-height: 1;
  }
  .contact__title { font-size: 13px; letter-spacing: 2px; margin-top: 4px; margin-bottom: 14px; }
  .contact__list { list-style: none; }
  .contact__item {
    display: flex; align-items: center; gap: 14px;
    font-size: 13px; letter-spacing: 2px; line-height: 22px;
  }
  .contact__item svg { width: 14px; height: 14px; fill: var(--navy); flex: none; }
  .contact__address { font-size: 13px; letter-spacing: 2px; line-height: 20px; margin-top: 10px; }
</style>
</head>
<body>
<main class="stage">

  <section class="card card--front">
    <div class="brand">
      <div class="brand__row">
        <span class="brand__dot"></span>
        <span class="brand__name">Birchlane Furnishing</span>
      </div>
      <span class="brand__tagline">Trade Furniture Solutions</span>
    </div>
    <p class="site">www.birchlane.co.uk</p>
  </section>

  <section class="card card--back">
    <div class="brand">
      <div class="brand__row">
        <span class="brand__dot"></span>
        <span class="brand__name">Birchlane Furnishing</span>
      </div>
      <span class="brand__tagline">Trade Furniture Solutions</span>
    </div>

    <div class="contact">
      <h1 class="contact__name">Alex Morgan</h1>
      <p class="contact__title">Manager</p>
      <ul class="contact__list">
        <li class="contact__item">
          <svg viewBox="0 0 24 24"><path d="M6.6 10.8a15.1 15.1 0 0 0 6.6 6.6l2.2-2.2c.3-.3.7-.4 1-.2 1.1.4 2.3.6 3.6.6.6 0 1 .4 1 1V20c0 .6-.4 1-1 1A17 17 0 0 1 3 4c0-.6.4-1 1-1h3.5c.6 0 1 .4 1 1 0 1.3.2 2.5.6 3.6.1.3 0 .7-.2 1z"/></svg>
          020 7946 0231
        </li>
        <li class="contact__item">
          <svg viewBox="0 0 24 24"><path d="M7 3h10v5H7zM4 9h16a2 2 0 0 1 2 2v7h-4v3H6v-3H2v-7a2 2 0 0 1 2-2zm4 7v3h8v-3z"/></svg>
          020 7946 0232
        </li>
        <li class="contact__item">
          <svg viewBox="0 0 24 24"><path d="M2 4h20v16H2zm2 2v.5l8 5.5 8-5.5V6zm0 3v9h16V9l-8 5.5z"/></svg>
          alex@birchlane.co.uk
        </li>
        <li class="contact__item">
          <svg viewBox="0 0 24 24"><path d="M12 2a10 10 0 1 0 0 20 10 10 0 0 0 0-20zm-1 17.9A8 8 0 0 1 4.2 10L9 15v1a2 2 0 0 0 2 2zm6.9-2.5A2 2 0 0 0 16 16h-1v-3a1 1 0 0 0-1-1H8v-2h2a1 1 0 0 0 1-1V7h2a2 2 0 0 0 2-2v-.4a8 8 0 0 1 2.9 12.8z"/></svg>
          www.birchlane.co.uk
        </li>
      </ul>
      <p class="contact__address">7B Harrow Lane Trade Estate<br>Northfield, London N9 4QX</p>
    </div>
  </section>

</main>
</body>
</html>
```